CD-/Plattencover für Tonträgerfirma
Zielgruppe
Wir sind eine Tonträgerfirma und bewegen uns im Low-Budget-Segment.
Aufgabenstellung
Für eine KLassik Serie benötigen wir 7 Cover, welche aber im Grundlayout immer gleich seinen sollten. Es soll eine erkenntliche Serie entstehen.
Das Thema lautet: Velvet Hour
Die Unterthemen lauten:
1. The Amber Lantern Gathering
2. The Velvet Hour Riverside Suites
3. The Velvet Hour Meadow Steps
4. The Velvet Hour Moonlit Whispers
5. The Copper Table Evenings
6. The Silver Curtain Soirée
7. The Northwind Orchestral Treasures
Wir benötigen nicht das komplette Artwork, sondern ein Frontcover
(12 x 12 cm + 2 cm Beschnitt wg. etwaiger Verschiebung der Positionierung
Fertigstellung (Aufziehen des Inlays und Labels) erfolgt später bei uns im Hause
Wir benötigen später offene psd-Dateien mit allen Ebenen
Wichtig: Schriften nicht gerastert ggfs. Schrift mitliefern

```html
<!DOCTYPE html>
<html lang="en">
<head>
<meta charset="utf-8">
<title>Velvet Hour – Classical Series Covers</title>
<link rel="stylesheet" href="https://fonts.googleapis.com/css2?family=Dancing+Script:wght@400&family=Lato:wght@400&display=swap">
<style>
  :root {
    --paper: #ffffff;
    --ink: #1a1a1a;
    --tone-1: #d4d4d4;
    --tone-2: #b8b8b8;
    --tone-3: #9c9c9c;
    --tone-4: #7e7e7e;
    --tone-5: #5c5c5c;
    --tone-6: #444444;
    --disc-red: #be1622;
    --disc-rim: #7a7a7a;
    --hub: #7c7d7e;
    --hole: #4a4a4a;
    --red: #be1622;
    --orange: #e8542a;
    --yellow: #f3e525;
    --green: #3aa935;
    --cyan: #1ea0dc;
    --navy: #2b3180;
    --purple: #8e2481;
  }
  * { margin: 0; padding: 0; box-sizing: border-box; }
  html, body { width: 849px; height: 1200px; overflow: hidden; background: var(--paper); }
  .sheet { position: relative; width: 849px; height: 1200px; }

  .cover {
    position: absolute;
    background: var(--paper);
    box-shadow: 2px 3px 5px rgba(0,0,0,0.18);
    overflow: hidden;
  }
  .cover-pattern { position: absolute; inset: 0; }

  /* Tonal fills standing in for each cover's line artwork */
  .pattern-diamond {
    background:
      linear-gradient(45deg, transparent 35%, rgba(0,0,0,0.16) 50%, transparent 65%),
      linear-gradient(-45deg, transparent 35%, rgba(0,0,0,0.16) 50%, transparent 65%),
      radial-gradient(closest-side at 50% 50%, var(--tone-4), var(--tone-2));
  }
  .pattern-circles {
    background: radial-gradient(circle at 50% 50%, var(--tone-5) 0%, var(--tone-4) 18%, var(--tone-2) 60%, var(--tone-3) 100%);
  }
  .pattern-waves {
    background: linear-gradient(180deg, var(--tone-3) 0%, var(--tone-2) 35%, var(--tone-3) 65%, var(--tone-2) 100%);
  }
  .pattern-dots {
    background: linear-gradient(180deg, var(--tone-5), var(--tone-6));
  }
  .pattern-zigzag {
    background: linear-gradient(135deg, var(--tone-2) 0%, var(--tone-3) 55%, var(--tone-4) 100%);
  }
  .pattern-lines {
    background: linear-gradient(180deg, var(--tone-1) 0%, var(--tone-2) 60%, var(--tone-3) 100%);
  }
  .pattern-hexagons {
    background: radial-gradient(ellipse 46% 52% at 50% 50%, var(--tone-5) 0%, var(--tone-3) 55%, var(--tone-1) 100%);
  }

  .title-plate {
    position: absolute;
    left: 0;
    top: 75.4%;
    height: 12.7%;
    display: flex;
    align-items: stretch;
    background: var(--paper);
    padding-right: 0.9em;
  }
  .title-plate .accent { width: 0.8em; flex: none; background: var(--accent); }
  .title-plate .wording { padding-left: 0.55em; display: flex; flex-direction: column; justify-content: center; }
  .series-line { font-family: "Lato", sans-serif; font-size: 1em; line-height: 1; color: var(--ink); padding-left: 0.95em; white-space: nowrap; }
  .album-line { font-family: "Dancing Script", cursive; font-size: 1.5em; line-height: 1.05; color: var(--ink); white-space: nowrap; }

  .cover-small { width: 243px; height: 243px; font-size: 8px; }
  .cover-large { left: 187px; top: 176px; width: 309px; height: 309px; font-size: 10.5px; z-index: 2; }
  .cover-large .title-plate { left: 2px; min-width: 151px; }

  .disc { position: absolute; left: 381px; top: 184px; width: 300px; height: 300px; z-index: 1; }
  .disc svg { position: absolute; inset: 0; }
  .disc-label { position: absolute; left: 112px; top: 218px; color: #fff; }
  .disc-label .series-line { color: #fff; font-size: 10px; padding-left: 0.9em; }
  .disc-label .album-line { color: #fff; font-size: 15px; }

  .row-1 { top: 575px; }
  .row-2 { top: 855px; }
  .col-1 { left: 25px; }
  .col-2 { left: 303px; }
  .col-3 { left: 581px; }
</style>
</head>
<body>
<main class="sheet">

  <section class="disc">
    <svg viewBox="0 0 300 300" aria-hidden="true">
      <circle cx="150" cy="150" r="148" fill="var(--disc-red)" stroke="var(--disc-rim)" stroke-width="2"/>
      <circle cx="150" cy="150" r="44" fill="var(--hub)"/>
      <circle cx="150" cy="150" r="17" fill="var(--hole)"/>
    </svg>
    <div class="disc-label">
      <p class="series-line">The Amber</p>
      <p class="album-line">Lantern Gathering</p>
    </div>
  </section>

  <article class="cover cover-large" style="--accent: var(--red)">
    <div class="cover-pattern pattern-diamond" role="img" aria-label="Black and white line pattern of nested diamonds"></div>
    <div class="title-plate"><span class="accent"></span><div class="wording"><p class="series-line">The Amber</p><p class="album-line">Lantern Gathering</p></div></div>
  </article>

  <article class="cover cover-small row-1 col-1" style="--accent: var(--orange)">
    <div class="cover-pattern pattern-circles" role="img" aria-label="Black and white line pattern of concentric circles"></div>
    <div class="title-plate"><span class="accent"></span><div class="wording"><p class="series-line">The Velvet Hour</p><p class="album-line">Riverside Suites</p></div></div>
  </article>

  <article class="cover cover-small row-1 col-2" style="--accent: var(--yellow)">
    <div class="cover-pattern pattern-waves" role="img" aria-label="Black and white pattern of wavy lines"></div>
    <div class="title-plate"><span class="accent"></span><div class="wording"><p class="series-line">The Velvet Hour</p><p class="album-line">Meadow Steps</p></div></div>
  </article>

  <article class="cover cover-small row-1 col-3" style="--accent: var(--green)">
    <div class="cover-pattern pattern-dots" role="img" aria-label="Dense black dot grid pattern"></div>
    <div class="title-plate"><span class="accent"></span><div class="wording"><p class="series-line">The Velvet Hour</p><p class="album-line">Moonlit Whispers</p></div></div>
  </article>

  <article class="cover cover-small row-2 col-1" style="--accent: var(--cyan)">
    <div class="cover-pattern pattern-zigzag" role="img" aria-label="Black and white zigzag line pattern"></div>
    <div class="title-plate"><span class="accent"></span><div class="wording"><p class="series-line">The Copper</p><p class="album-line">Table Evenings</p></div></div>
  </article>

  <article class="cover cover-small row-2 col-2" style="--accent: var(--navy)">
    <div class="cover-pattern pattern-lines" role="img" aria-label="Black and white pattern of fine horizontal lines"></div>
    <div class="title-plate"><span class="accent"></span><div class="wording"><p class="series-line">The Silver</p><p class="album-line">Curtain Soirée</p></div></div>
  </article>

  <article class="cover cover-small row-2 col-3" style="--accent: var(--purple)">
    <div class="cover-pattern pattern-hexagons" role="img" aria-label="Black and white line pattern of nested hexagons"></div>
    <div class="title-plate"><span class="accent"></span><div class="wording"><p class="series-line">The Northwind</p><p class="album-line">Orchestral Treasures</p></div></div>
  </article>

</main>
</body>
</html>
```